Tri-Fold Menu of Services for our Eyelash and Skin Care Spa

We need a beautiful spa service menu for our upscale spa in St. Charles Missouri. We specialize in providing treatments that are specific to the clients needs. Our services are eyelash extensions, skin care treatments, full body waxing and makeup application. Our spa colors are dark purples and greys and we are not opposed to additional colors that would complement those colors. We do a lot of eyelash extensions and while we do what those services listed we would like the skin care treatments to be in an area that would be noticed first. One of the attachments lists all of our services, descriptions and prices (please be sure to include all services and pricing. descriptions if possible). And our website has more information about us if needed. The website was not professionally done. So it DOESN'T represent our style exactly.

I HAVE ATTACHED A FEW PHOTOS BUT THEY DON'T HAVE TO BE USED.

Target Market(s)

women who would like to look their best, 35-55, annual income of 100,000+, she is usually busy and her children (if she has any) are high school age or older.

Industry/Entity Type

It Service

Font styles to use
Serif
Sans Serif

Requirements
Must have
• Must list all of our services. If it works to have the descriptions that would be great.
Nice to have
• If it works to have the descriptions of each service that would be great.

```html
<!DOCTYPE html>
<html lang="en">
<head>
<meta charset="utf-8">
<title>Lumera Lash &amp; Skin Spa – Service Menu</title>
<link href="https://fonts.googleapis.com/css2?family=Cabin:wght@400;500;600&display=swap" rel="stylesheet">
<style>
:root{
  --purple:#55206e;
  --frame:#4b5358;
  --slate:#5f676d;
  --mist:#a9afb4;
  --paper:#ffffff;
  --ink:#4f5356;
  --bg-light:#f4f5f6;
}
*{box-sizing:border-box;margin:0;padding:0}
html,body{width:1200px;height:927px;overflow:hidden}
body{font-family:"Cabin",sans-serif;color:var(--ink);background:var(--bg-light)}
.brochure{position:relative;width:1200px;height:927px;overflow:hidden}
.panel{position:absolute;top:0;height:927px;width:400px}
.panel--left{left:0;background:linear-gradient(90deg,#f7f8f8,#e6e8ea)}
.panel--middle{left:400px;background:linear-gradient(180deg,#e9ebec,#d9dcde)}
.panel--cover{left:800px;background:var(--paper)}
.abs{position:absolute}
.photo{position:absolute}
.frame{position:absolute;border:3px solid var(--frame);background:var(--paper)}
.heading{position:absolute;background:var(--purple);color:#fff;text-align:center;font-weight:400;letter-spacing:.5px}
.heading::after{content:"";position:absolute;left:0;right:0;bottom:-5px;height:2px;background:var(--purple)}
.price{color:var(--purple);font-weight:500}
.lash-list{position:absolute;left:46px;width:308px;text-align:center}
.lash-list h3{font-weight:400;font-size:18px;color:#3b3e40;margin-bottom:2px}
.lash-list p{font-size:13px;line-height:17.5px}
.lash-list .price{font-size:16.5px}
.wax-row{position:absolute;font-size:13.5px;height:17px;line-height:17px}
.wax-row .price{position:absolute;right:0;font-size:16px}
.massage{position:absolute;left:400px;top:646px;width:400px;height:226px;background:var(--slate);color:#eef0f1}
.massage h2{position:absolute;left:0;right:0;top:16px;text-align:center;font-weight:400;font-size:29px;letter-spacing:.5px;color:#fff}
.massage .rule{position:absolute;left:38px;right:38px;top:54px;height:1px;background:#d6d9db}
.m-row{position:absolute;left:38px;width:322px;font-size:13px;line-height:15.5px}
.m-row span:last-child{position:absolute;right:0;bottom:0}
.m-note{position:absolute;left:38px;width:324px;top:163px;font-size:11.6px;line-height:15.3px}
.mini-mark{position:absolute;left:400px;top:872px;width:400px;height:55px;background:var(--mist);text-align:center;line-height:55px;font-size:13px;color:var(--purple)}
.band{position:absolute;left:800px;width:400px;background:var(--purple)}
.brand{position:absolute;left:800px;top:120px;width:400px;text-align:center;color:var(--purple)}
.brand .name{font-size:52px;font-weight:500;letter-spacing:1px;line-height:56px}
.brand .sub{font-size:17px;font-weight:500;margin-top:2px}
.contact{position:absolute;left:800px;top:712px;width:400px;text-align:center;font-size:13.6px;line-height:16.8px;color:#2f3234}
.web{position:absolute;left:800px;top:822px;width:400px;text-align:center;font-size:20px;color:var(--purple);font-weight:500}
</style>
</head>
<body>
<div class="brochure">
  <section class="panel panel--left">
    <div class="frame" style="left:46px;top:54px;width:308px;height:821px"></div>
    <div class="photo" role="img" aria-label="Close-up of an eye with long lash extensions" style="left:49px;top:57px;width:302px;height:184px;background:linear-gradient(135deg,#cdb8ae,#e7d9d3 55%,#6a5b58)"></div>
    <h2 class="heading" style="left:71px;top:218px;width:258px;height:44px;line-height:44px;font-size:29px">EYELASHES</h2>
    <div class="lash-list" style="top:271px">
      <h3>Classic</h3>
      <p>Full Set <span class="price">$175</span></p>
      <p>Demi Set <span class="price">$110</span></p>
      <p>Touch up <span class="price">$60</span></p>
      <h3 style="margin-top:9px">Volume Technique</h3>
      <p>Full Set <span class="price">$220</span></p>
      <p>Demi Set <span class="price">$135</span></p>
      <p>Touch up <span class="price">$72</span></p>
    </div>
    <h2 class="heading" style="left:71px;top:453px;width:258px;height:45px;line-height:45px;font-size:29px">TINTING</h2>
    <div class="lash-list" style="top:512px">
      <p>Eyebrows <span class="price">$20</span></p>
      <p>Eyelashes <span class="price">$20</span></p>
      <p>Both <span class="price">$30</span></p>
    </div>
    <div class="photo" role="img" aria-label="Woman having powder applied with a makeup brush" style="left:49px;top:581px;width:302px;height:291px;background:linear-gradient(120deg,#b8a89c,#efe2da 45%,#e9d6cc)"></div>
  </section>

  <section class="panel panel--middle">
    <div class="frame" style="left:46px;top:54px;width:308px;height:392px"></div>
    <h2 class="heading" style="left:72px;top:76px;width:257px;height:47px;line-height:47px;font-size:29px">WAXING</h2>
    <div class="abs" style="left:70px;top:143px;width:120px">
      <div class="wax-row" style="top:0;width:120px">Eyebrows<span class="price">$17</span></div>
      <div class="wax-row" style="top:17.3px;width:120px">Upper Lip<span class="price">$14</span></div>
      <div class="wax-row" style="top:34.6px;width:120px">Chin<span class="price">$14</span></div>
      <div class="wax-row" style="top:51.9px;width:120px">Sides of face<span class="price">$14</span></div>
      <div class="wax-row" style="top:69.2px;width:120px">Bikini<span class="price">$27+</span></div>
      <div class="wax-row" style="top:86.5px;width:120px">Brazilian<span class="price">$55+</span></div>
      <div class="wax-row" style="top:103.8px;width:120px">Underarm<span class="price">$22</span></div>
    </div>
    <div class="abs" style="left:210px;top:143px;width:121px">
      <div class="wax-row" style="top:0;width:121px">Arms Full<span class="price">$35</span></div>
      <div class="wax-row" style="top:17.3px;width:121px">Lower<span class="price">$26</span></div>
      <div class="wax-row" style="top:34.6px;width:121px">Legs Full<span class="price">$62</span></div>
      <div class="wax-row" style="top:51.9px;width:121px">Lower<span class="price">$40</span></div>
      <div class="wax-row" style="top:69.2px;width:121px">Chest<span class="price">$44</span></div>
      <div class="wax-row" style="top:86.5px;width:121px">Back<span class="price">$44</span></div>
    </div>
    <div class="photo" role="img" aria-label="Beach scene with straw bag, sun hat, sunglasses and flip-flops" style="left:49px;top:268px;width:302px;height:175px;background:linear-gradient(180deg,#ffffff,#d7e6ea 35%,#ece4d8 70%,#c9a56e)"></div>
    <div class="photo" role="img" aria-label="Woman receiving a back massage" style="left:0;top:458px;width:400px;height:188px;background:linear-gradient(120deg,#f2ece6,#d9a583 45%,#f4eee9)"></div>
  </section>
  <div class="massage">
    <h2>MASSAGE</h2>
    <div class="rule"></div>
    <div class="m-row" style="top:66px"><span>Neck, Back &amp; Head Massage</span><span>$45 | 30 minutes</span></div>
    <div class="m-row" style="top:86px"><span>Aromatherapy Scalp Massage</span><span>$15 | 10 minutes</span></div>
    <div class="m-row" style="top:105px"><span>Foot Massage and Scrub</span><span>$20 | 15 minutes</span></div>
    <div class="m-row" style="top:125px"><span>Headache &amp; Migraine<br>Relief Treatment *</span><span>$45 | 30 minutes</span></div>
    <p class="m-note">* Relief from headaches caused by stress, tension, hormonal imbalances or sensitivities using cold stones and massaging techniques for the face.</p>
  </div>
  <div class="mini-mark">Lumera Lash &amp; Skin Spa</div>

  <section class="panel panel--cover"></section>
  <div class="band" style="top:0;height:54px"></div>
  <div class="abs" style="left:800px;top:54px;width:400px;height:13px;background:var(--mist)"></div>
  <div class="brand">
    <div class="name">Lumera</div>
    <div class="sub">Lash &amp; Skin Spa</div>
  </div>
  <div class="photo" role="img" aria-label="Woman relaxing during a facial massage" style="left:800px;top:290px;width:400px;height:398px;background:linear-gradient(110deg,#f6f1ee,#e4c1a8 50%,#f3ede9)"></div>
  <div class="abs" style="left:800px;top:688px;width:400px;height:2px;background:var(--mist)"></div>
  <div class="contact">
    2240 Harlow Ln, Maple Ridge MO 63410<br>
    (Across Route 12 from Summit Fitness)<br>
    Tel: 555 014 2287<br>
    Email: lumeraspa@mail.com
  </div>
  <div class="web">www.lumeraspa.com</div>
  <div class="band" style="top:872px;height:55px"></div>
</div>
</body>
</html>
```